Tidal Fern Business Cards

We need something new, fun and exciting for business cards. Our current ones are just plain and we need a design that pops. We want name, position held, phone, email on the front, and a 20% discount on the back. I have also uploaded our old business cards creative to see what we are not wanting, and how boring they were and we want something jazzed up from this, cool design and catches people attention.

```html
<!DOCTYPE html>
<html lang="en">
<head>
<meta charset="utf-8">
<title>Tidal Fern Business Cards</title>
<link rel="stylesheet" href="https://fonts.googleapis.com/css2?family=Montserrat:wght@400;500;700;800&display=swap">
<style>
  :root {
    --navy: #163d6e;
    --coral: #f0716d;
    --white: #ffffff;
    --paper: #f4f4f2;
    --ink: #1f2a3a;
  }
  * { box-sizing: border-box; margin: 0; padding: 0; }
  html, body {
    width: 1200px; height: 895px; overflow: hidden;
    background: var(--paper);
    font-family: "Montserrat", sans-serif;
  }
  .canvas {
    position: relative; width: 1200px; height: 895px;
  }
  .card {
    position: absolute; left: 250px;
    width: 700px; height: 400px; overflow: hidden;
    box-shadow: 0 6px 18px rgba(0,0,0,0.12);
  }
  .card--back { top: 30px; background: var(--navy); }
  .card--front { top: 465px; background: var(--white); }

  .discount-corner {
    position: absolute; inset: 0; width: 100%; height: 100%;
  }
  .discount {
    position: absolute; left: 40px; top: 190px;
    transform: rotate(-90deg); transform-origin: left top;
    color: var(--white); line-height: 1;
  }
  .discount__value { font-weight: 800; font-size: 58px; display: block; }
  .discount__label { font-weight: 400; font-size: 27px; display: block; margin-top: 4px; }

  .brand {
    display: flex; align-items: center; gap: 16px;
    font-weight: 700; letter-spacing: 0.5px; line-height: 1;
  }
  .brand__dot { border-radius: 50%; background: var(--coral); flex: none; }

  .card--back .brand {
    position: absolute; right: 60px; top: 160px;
    color: var(--white); font-size: 50px;
  }
  .card--back .brand__dot { width: 30px; height: 30px; }

  .card--front .brand {
    position: absolute; left: 120px; top: 105px;
    color: var(--navy); font-size: 72px;
  }
  .card--front .brand__dot { width: 46px; height: 46px; }

  .contact {
    position: absolute; left: 262px; top: 205px; color: var(--ink);
  }
  .contact__name {
    font-weight: 800; font-size: 24px; color: var(--navy); letter-spacing: 0.5px;
  }
  .contact__role { font-weight: 400; font-size: 18px; margin-top: 4px; letter-spacing: 0.5px; }
  .contact__list { list-style: none; margin-top: 20px; }
  .contact__item {
    display: flex; align-items: center; gap: 12px;
    font-size: 17px; letter-spacing: 0.6px; margin-bottom: 8px;
  }
  .contact__icon { width: 24px; height: 24px; flex: none; }
</style>
</head>
<body>
<main class="canvas">
  <section class="card card--back" aria-label="Card back">
    <svg class="discount-corner" viewBox="0 0 700 400" preserveAspectRatio="none" aria-hidden="true">
      <polygon points="0,0 252,0 0,248" fill="var(--coral)"/>
    </svg>
    <p class="discount">
      <span class="discount__value">20%</span>
      <span class="discount__label">Discount</span>
    </p>
    <div class="brand"><span class="brand__dot"></span>Tidal Fern</div>
  </section>

  <section class="card card--front" aria-label="Card front">
    <div class="brand"><span class="brand__dot"></span>Tidal Fern</div>
    <div class="contact">
      <h1 class="contact__name">MARCUS HALE</h1>
      <p class="contact__role">Founder and CEO</p>
      <ul class="contact__list">
        <li class="contact__item">
          <svg class="contact__icon" viewBox="0 0 24 24" aria-hidden="true">
            <circle cx="12" cy="12" r="12" fill="var(--coral)"/>
            <path d="M6 10c0-2 3-3 6-3s6 1 6 3l-2 1-1-2h-6l-1 2z M8 12h8l1 5H7z" fill="var(--white)"/>
            <circle cx="12" cy="14.5" r="1.5" fill="var(--coral)"/>
          </svg>
          <span>000 000 0000</span>
        </li>
        <li class="contact__item">
          <svg class="contact__icon" viewBox="0 0 24 24" aria-hidden="true">
            <circle cx="12" cy="12" r="12" fill="var(--coral)"/>
            <rect x="6" y="8" width="12" height="8" fill="none" stroke="var(--white)" stroke-width="1.5"/>
            <path d="M6 8l6 5 6-5" fill="none" stroke="var(--white)" stroke-width="1.5"/>
          </svg>
          <span>m_hale@tidalfern.com.au</span>
        </li>
      </ul>
    </div>
  </section>
</main>
</body>
</html>
```